PEACFUL ACUPUNCTURE PRACTITIONER NEEDS A NEW COAT

I need a new design for an exiting website http://willowgateneedlework.com/ for a acupuncturist. This will be a minimalism design with lots and lots of white space. Home page and one interior page. Please keep the feeling of calm and peaceful serenity. For Color scheme: https://www.morningfernclinic.com/fertility. The bottom part of the home page with sections and links to the service pages: https://harborlotuswellness.com/. The client likes this the best: http://mfclinic.com/. I'm attaching the logo and content pages.

Target Market(s)

Women

Industry/Entity Type

Wellness, health, wellbeing, meditation

Number of Pages Required

2 page

Font styles to use
Sans Serif
Decorative

Colors

Designer to choose colors to be used in the design.

Requirements
Must have
Nice to have
• Follow new website drafts and links
Should not have
• Busy with bright colors. No poping

```html
<!DOCTYPE html>
<html lang="en">
<head>
<meta charset="utf-8">
<title>Willowgate Acupuncture</title>
<link rel="stylesheet" href="https://fonts.googleapis.com/css2?family=Montserrat:wght@400;500;600;800&display=swap">
<style>
:root{
  --mauve:#bf868d;
  --mauve-light:#d9b3b7;
  --gold:#d8b56c;
  --cream:#f1e0bd;
  --ink:#1f1f1f;
  --body:#333;
  --soft:#f8f8f8;
  --dark:#3b3a3a;
  --button:#565656;
  --slate:#7f8eaa;
  --pink:#d79ab4;
  --amber:#d9a93f;
  --teal:#7ea79b;
}
*{box-sizing:border-box;margin:0;padding:0}
html,body{width:1200px;height:2215px;overflow:hidden}
body{position:relative;background:#fff;font-family:'Montserrat',sans-serif;color:var(--body)}
.abs{position:absolute}
a{color:inherit;text-decoration:none}

/* header */
.top-phone{left:95px;top:37px;font-size:14px;color:var(--mauve);display:flex;align-items:center;gap:7px}
.brand{left:0;width:1200px;top:22px;text-align:center;display:flex;justify-content:center;align-items:center;gap:12px}
.brand-dot{width:34px;height:34px;border-radius:50%;background:var(--mauve-light)}
.brand-name{font-size:28px;font-weight:500;color:#555;letter-spacing:.5px}
.social{display:flex;gap:18px}
.social span{width:12px;height:12px;border-radius:50%;background:var(--mauve)}
.top-social{left:1000px;top:41px}

/* nav */
.nav{left:88px;top:94px;width:1024px;height:40px;background:var(--mauve);display:flex;align-items:center;padding-left:18px}
.nav a{color:#fff;font-size:13px;padding:7px 14px}
.nav a.active{background:var(--mauve-light);color:#4a3a3c;border-radius:3px}

/* hero */
.hero{left:0;top:134px;width:1200px;height:478px;background:radial-gradient(ellipse at 55% 40%,#f1c9b6 0%,#e4b3a3 35%,#c89283 70%,#b98a80 100%)}
.edge-band{left:0;width:1200px;height:4px;background:var(--cream)}
.hero-text{left:0;width:1200px;top:328px;text-align:center;color:var(--ink)}
.hero-text h1{font-size:37px;font-weight:800;line-height:1}
.hero-text p{font-size:24px;margin-top:6px;color:#111}
.btn{display:inline-block;margin-top:22px;background:var(--button);color:#fff;font-size:15px;font-weight:500;padding:10px 23px;border-radius:2px}

/* philosophy */
.philo-img{left:154px;top:695px;width:380px;height:334px;background:linear-gradient(160deg,#6f7a55 0%,#d9c48e 45%,#efe6d6 70%,#d8cbb3 100%);box-shadow:0 4px 18px rgba(0,0,0,.08)}
.philo{left:613px;top:770px;width:445px}
.section-title{font-size:32px;font-weight:600;color:var(--gold)}
.philo p{margin-top:16px;font-size:15px;line-height:22.5px;color:#2b2b2b}

/* services */
.services{left:0;top:1110px;width:1200px;height:793px;background:var(--soft)}
.services-title{left:0;width:1200px;top:1183px;text-align:center}
.card-img{width:374px;height:216px}
.card-label{width:255px;height:53px;background:#fff;border-left:8px solid;font-size:18px;font-weight:600;color:var(--ink);padding:15px 0 0 18px;box-shadow:0 3px 10px rgba(0,0,0,.05);letter-spacing:.3px}

/* footer */
.footer{left:0;top:1903px;width:1200px;height:273px;background:var(--dark)}
.foot-brand{left:88px;top:1985px;width:225px;text-align:center}
.foot-brand .brand-dot{margin:0 auto 12px;width:58px;height:58px}
.foot-brand div.name{font-size:28px;font-weight:500;color:#fff;line-height:1.15}
.foot-title{font-size:18px;font-weight:600;color:var(--gold)}
.foot-links{display:grid;grid-template-columns:222px 200px;row-gap:12px;margin-top:16px;font-size:13.5px;color:#fff}
.foot-links a.current{color:var(--mauve-light);text-decoration:underline}
.contact-row{display:flex;gap:14px;font-size:13.5px;color:#fff;line-height:20px;margin-top:14px}
.contact-row svg{flex:none;margin-top:2px}
.bottom-bar{left:0;top:2176px;width:1200px;height:39px;background:var(--mauve);color:#fff;font-size:13px;padding:11px 88px;display:flex;justify-content:space-between;align-items:center}
.bottom-bar .social span{background:#fff}
</style>
</head>
<body>

<header>
  <a class="abs top-phone" href="#">
    <svg width="14" height="14" viewBox="0 0 24 24"><path fill="#bf868d" d="M6.6 10.8a15 15 0 0 0 6.6 6.6l2.2-2.2c.3-.3.7-.4 1-.2 1.1.4 2.3.6 3.6.6.6 0 1 .4 1 1V20c0 .6-.4 1-1 1A17 17 0 0 1 3 4c0-.6.4-1 1-1h3.5c.6 0 1 .4 1 1 0 1.3.2 2.5.6 3.6.1.3 0 .7-.2 1z"/></svg>
    413-555-0142
  </a>
  <div class="abs brand"><span class="brand-dot"></span><span class="brand-name">Willowgate Acupuncture</span></div>
  <div class="abs social top-social"><span></span><span></span><span></span><span></span></div>
</header>

<nav class="abs nav">
  <a class="active" href="#">Home</a><a href="#">About</a><a href="#">Fertility &amp; Pregnancy</a><a href="#">Hormone Balance</a><a href="#">Strength &amp; Structure</a><a href="#">Emotional wellbeing</a><a href="#">Online Shop</a><a href="#">Testimonials</a>
</nav>

<section class="abs hero" role="img" aria-label="Soft close-up photograph of a newborn's feet held in a parent's hands"></section>
<div class="abs edge-band" style="top:608px"></div>
<div class="abs hero-text">
  <h1>Welcome to</h1>
  <p>Willowgate Acupuncture</p>
  <a class="btn" href="#">Contact Us</a>
</div>

<section>
  <div class="abs philo-img" role="img" aria-label="Photograph of a woman meditating cross-legged on a sunlit beach"></div>
  <div class="abs philo">
    <h2 class="section-title">Philosophy of Care</h2>
    <p>Since our beginning, Atlanta homeowners have continually enjoyed personalized home cleaning service with a pristine difference. Our pricing plans are affordable with easy online booking wherever you are in Metro Atlanta, Atlanta and its surroundings.</p>
  </div>
</section>

<section class="abs services"></section>
<h2 class="abs section-title services-title">Our Services</h2>

<div class="abs card-img" style="left:206px;top:1275px;background:linear-gradient(180deg,#d9a63e 0%,#e7c9b0 50%,#3f67a8 100%)" role="img" aria-label="Photograph of a couple's hands forming a heart on a pregnant belly"></div>
<div class="abs card-label" style="left:206px;top:1468px;border-color:var(--slate)">Fertility &amp; Pregnancy</div>

<div class="abs card-img" style="left:620px;top:1275px;background:linear-gradient(135deg,#8fa7b0 0%,#c55a6a 45%,#9a8dd6 70%,#3fa3c1 100%)" role="img" aria-label="Photograph of hands holding blocks reading hormone balance"></div>
<div class="abs card-label" style="left:620px;top:1468px;border-color:var(--pink)">Hormone Balance</div>

<div class="abs card-img" style="left:206px;top:1562px;background:linear-gradient(120deg,#8094b2 0%,#9b9797 45%,#e4e7ea 100%)" role="img" aria-label="Photograph of a doctor listening to a pregnant belly with a stethoscope"></div>
<div class="abs card-label" style="left:206px;top:1755px;border-color:var(--amber)">Strength &amp; Structure</div>

<div class="abs card-img" style="left:620px;top:1562px;background:linear-gradient(120deg,#bdb3a6 0%,#d8d2c8 50%,#eae2d8 100%)" role="img" aria-label="Photograph of a relaxed pregnant woman resting on a sofa at home"></div>
<div class="abs card-label" style="left:620px;top:1755px;border-color:var(--teal)">Emotional wellbeing</div>

<footer>
  <div class="abs footer"></div>
  <div class="abs edge-band" style="top:1899px"></div>

  <div class="abs foot-brand">
    <div class="brand-dot"></div>
    <div class="name">Willowgate<br>Acupuncture</div>
  </div>

  <div class="abs" style="left:400px;top:1955px">
    <h3 class="foot-title">Quick Link</h3>
    <div class="foot-links">
      <a href="#">Home</a><a href="#">Emotional wellbeing</a>
      <a href="#">About</a><a href="#">Online Shop</a>
      <a class="current" href="#">Fertility &amp; Pregnancy</a><a href="#">Testimonials</a>
      <a href="#">Hormone Balance</a><a href="#">Contact Us</a>
      <a href="#">Strength &amp; Structure</a>
    </div>
  </div>

  <div class="abs" style="left:840px;top:1955px">
    <h3 class="foot-title">Conatct info</h3>
    <div class="contact-row">
      <svg width="16" height="20" viewBox="0 0 24 30"><path fill="#bf868d" d="M12 0a10 10 0 0 0-10 10c0 7.5 10 20 10 20s10-12.5 10-20A10 10 0 0 0 12 0zm0 14a4 4 0 1 1 0-8 4 4 0 0 1 0 8z"/></svg>
      <span>48 Alder Row<br>Easthollow, MA 01077</span>
    </div>
    <div class="contact-row" style="margin-top:16px">
      <svg width="16" height="16" viewBox="0 0 24 24"><path fill="#bf868d" d="M6.6 10.8a15 15 0 0 0 6.6 6.6l2.2-2.2c.3-.3.7-.4 1-.2 1.1.4 2.3.6 3.6.6.6 0 1 .4 1 1V20c0 .6-.4 1-1 1A17 17 0 0 1 3 4c0-.6.4-1 1-1h3.5c.6 0 1 .4 1 1 0 1.3.2 2.5.6 3.6.1.3 0 .7-.2 1z"/></svg>
      <span>413-555-0142</span>
    </div>
    <div class="contact-row" style="margin-top:22px">
      <svg width="16" height="14" viewBox="0 0 24 18"><rect width="24" height="18" fill="#bf868d"/><path d="M1 1l11 9 11-9" fill="none" stroke="#3b3a3a" stroke-width="2"/></svg>
      <span>june@willowgateacupuncture.com</span>
    </div>
  </div>

  <div class="abs bottom-bar">
    <span>Copyright © 2021 Willowgate Acupuncture. All Rights Reserved</span>
    <div class="social"><span></span><span></span><span></span><span></span></div>
  </div>
</footer>

</body>
</html>
```